Redesign start page for existing online shop

We are selling building material (chimneys and flue pipes) as well as fireplaces (stoves). For this online shop we need a new start page. The domain is brunnfeld-bauwaren.de. Here you can see the current design. We want a smoother design with just one banner in the middle instead of the three in the first row. The look has to be more professional and trustworthy. You can therefore play with the colors. We want to try some different orange instead of our yellow / orange color. A few more things: - The phone number has to be bigger and more highlighted - So the 5 advantages at the top should be shown in a different way - New design for the products below - New footer

Target Market(s)

Germany and other countries in Europe.

Industry/Entity Type

Home Builder

Number of Pages Required

1 page

Other font styles liked:
• Please se the font on our current site.

Colors
f78f20
f68d4c

Requirements
Must have
• - Clear design - Trustworthy look - All elements Which are now shown shoulderstand be still there after redesigning -
Nice to have
• - See the Following sites to have a clou about our wishes: kalvesto.de flinkrabe.de

```html
<!DOCTYPE html>
<html lang="de">
<head>
<meta charset="utf-8">
<title>Brunnfeld Bauwaren – Edelstahlschornstein</title>
<link href="https://fonts.googleapis.com/css2?family=Open+Sans:wght@400;600;700;800&display=swap" rel="stylesheet">
<style>
:root{
  --orange:#f26b1d;
  --orange-soft:#f68d4c;
  --black:#0d0d0d;
  --panel:#1a1a1a;
  --line:#333;
  --text:#3a3a3a;
  --muted:#8a8a8a;
  --grey-band:#ececec;
  --grey-band2:#d9d9d9;
  --white:#fff;
}
*{box-sizing:border-box;margin:0;padding:0}
html,body{width:1200px;height:2885px;overflow:hidden}
body{font-family:"Open Sans",Arial,sans-serif;color:var(--text);background:var(--white);font-size:13px;line-height:1.5}
a{color:inherit;text-decoration:none}
.wrap{width:930px;margin:0 auto;position:relative}

/* top bar */
.topbar{height:27px;background:#000;color:#bbb;font-size:12px}
.topbar .wrap{width:1170px;display:flex;justify-content:space-between;align-items:center;height:27px}
.topbar .active{color:var(--white)}

/* header */
.header{height:92px;background:linear-gradient(#1e1e1e,#0e0e0e)}
.header .wrap{width:1120px;display:flex;align-items:center;height:92px}
.brand{display:flex;align-items:center;gap:12px;color:var(--white);font-weight:700;font-size:25px;line-height:1;text-transform:uppercase;letter-spacing:.5px}
.brand-dot{width:54px;height:54px;border-radius:50%;background:var(--orange)}
.brand small{display:block;font-size:25px;color:#ccc}
.phone{margin-left:auto;margin-right:30px;width:276px;height:58px;border-radius:8px;background:#2a2a2a;border:1px solid #444;display:flex;flex-direction:column;align-items:center;justify-content:center}
.phone strong{color:var(--orange);font-size:25px;font-weight:800;line-height:1}
.phone span{color:#aaa;font-size:11px}
.seal{width:60px;height:60px;border-radius:50%;background:#e0e0e0;border:4px solid #f2b91b;margin-right:26px}
.account{color:#ddd;font-size:13px;display:flex;flex-direction:column;gap:8px}
.account div{display:flex;align-items:center;gap:8px}
.account i{width:17px;height:17px;border-radius:50%;background:#f2b91b;display:inline-block}
.account a{text-decoration:underline}

/* nav */
.nav{height:39px;background:var(--orange)}
.nav .wrap{width:1200px;display:flex;align-items:center;height:39px}
.nav-item{height:39px;display:flex;align-items:center;padding:0 0 0 26px;width:152px;color:var(--white);font-weight:700;font-size:14px;background:var(--orange)}
.nav-item.dark{background:#151515;color:var(--orange);width:178px;justify-content:center;padding:0}
.nav-search{margin-left:auto;margin-right:30px;display:flex}
.nav-search span{width:156px;height:22px;background:var(--white);font-size:10px;color:#999;padding:3px 6px}
.nav-search b{width:22px;height:22px;background:#ddd;border:1px solid #888}

/* hero */
.hero{height:400px;background:radial-gradient(circle at 60% 40%,#222,#050505 70%)}
.hero .wrap{padding-top:24px}
.hero h1{color:var(--orange);font-size:29px;font-weight:700}
.hero-frame{position:absolute;left:0;top:86px;width:452px;height:304px;background:var(--white);padding:11px}
.hero-photo{width:100%;height:100%;background:linear-gradient(180deg,#8fb3d6 0%,#c9d9e6 40%,#b9552e 55%,#6d5a44 80%,#4e6b2f 100%)}
.hero-copy{position:absolute;left:475px;top:88px;color:var(--white);width:470px}
.hero-copy h2{font-size:19px;font-weight:400;line-height:1.4;margin-bottom:18px}
.hero-copy ul{list-style:none}
.hero-copy li{display:flex;align-items:center;gap:12px;font-size:16px;margin-bottom:23px}
.tick{width:20px;height:20px}
.cta{display:inline-flex;align-items:center;gap:18px;margin-top:4px}
.btn{background:var(--orange);color:var(--white);font-size:13px;padding:2px 12px;border-radius:2px;font-weight:600}
.cta em{font-style:normal;color:#aaa;font-size:17px;letter-spacing:2px}

/* intro */
.intro{height:472px;padding-top:44px}
.intro h3{font-size:15px;font-weight:700;color:#222;line-height:1.45;margin-bottom:14px}
.intro p{font-size:12.5px;line-height:1.55;color:#555;margin-bottom:16px}
.readmore{font-size:12px;color:#555;text-decoration:underline;font-style:italic}

/* features */
.features{height:278px;background:radial-gradient(circle at 50% 30%,#242424,#070707 75%)}
.features .wrap{display:flex;height:278px;padding-top:40px}
.feature{flex:1;text-align:center;color:var(--white);border-right:1px solid var(--line);padding-bottom:30px}
.feature:last-child{border-right:none}
.feature-icon{width:76px;height:76px;margin:0 auto 16px}
.feature h4{font-size:20px;font-weight:700;margin-bottom:6px}
.feature p{color:#999;font-size:13px;line-height:1.35;margin-bottom:14px}
.feature a{color:var(--orange);font-size:11px;text-decoration:underline}

/* products */
.products{height:817px;padding-top:48px}
.grid{display:grid;grid-template-columns:repeat(4,217px);grid-template-rows:217px 217px;gap:18px 20px}
.card{position:relative}
.card .shot{position:absolute;inset:0 0 22px 0}
.card-bar{position:absolute;left:0;right:0;bottom:0;height:22px;display:flex;justify-content:space-between;align-items:flex-end}
.see{background:#555;color:#eee;font-size:10px;padding:2px 8px;font-weight:600;margin-bottom:1px}
.see.hot{background:var(--orange);color:var(--white)}
.price{background:#000;color:var(--white);font-weight:700;font-size:17px;padding:1px 10px;height:28px;line-height:26px}
.card-featured{grid-column:1/3;grid-row:1/3;position:relative}
.card-featured .shot{position:absolute;left:0;top:0;width:454px;height:192px}
.caption{position:absolute;background:rgba(0,0,0,.82);color:var(--white)}
.caption h5{color:var(--orange);font-size:23px;font-weight:700;line-height:1.1}
.caption .stars{color:var(--orange);font-size:16px;letter-spacing:2px;position:absolute}
.caption p{font-size:10.5px;line-height:1.35;color:#ddd}
.cap-big{left:0;top:192px;width:454px;height:94px;padding:10px 12px}
.cap-big .stars{right:170px;top:10px}
.cap-big p{width:440px;margin-top:6px}
.feat-title{position:absolute;left:0;top:296px;font-size:17px;font-weight:700;color:#111}
.feat-price{position:absolute;right:0;top:274px;background:#000;color:var(--white);font-weight:700;font-size:22px;padding:2px 14px}
.feat-buy{position:absolute;right:0;top:312px;background:var(--orange);color:var(--white);font-weight:700;font-size:16px;padding:2px 20px}
.feat-text{position:absolute;left:0;top:328px;width:300px;font-size:10.5px;line-height:1.45;color:#555}
.feat-more{position:absolute;left:0;top:430px;font-size:11px;text-decoration:underline;font-style:italic;color:#555}
.divider{height:1px;background:#ddd;margin:26px 0 24px}
.row4{display:grid;grid-template-columns:repeat(4,217px);gap:20px;height:229px}
.row4 .card{height:229px}
.cap-small{left:0;top:118px;width:217px;height:88px;padding:6px 8px}
.cap-small h5{font-size:18px}
.cap-small .stars{right:50px;top:8px;font-size:12px}
.cap-small p{font-size:9.5px;margin-top:4px}

/* secure */
.secure{height:295px;background:var(--grey-band);padding-top:45px}
.secure-row{display:flex;align-items:flex-start}
.secure-label{width:247px;font-size:17px;font-weight:600;color:#222}
.flag-badge{width:72px;height:40px;background:#e2e2e2;border:2px solid #bbb;margin-right:14px;flex:none}
.secure-text{width:230px;font-size:10.5px;line-height:1.45;color:#666}
.round-badge{width:64px;height:64px;border-radius:50%;background:#2b2b2b;border:4px solid #c89b2e;margin:0 18px 0 64px;flex:none}
.pay-row{display:flex;align-items:center;margin-top:52px}
.pays{display:flex;gap:14px}
.pay{width:81px;height:48px;background:var(--white);border:1px solid #ccc;border-radius:3px;display:flex;align-items:center;justify-content:center;font-size:12px;font-weight:700;color:#333}

/* brands */
.brands{height:167px;background:var(--grey-band2);padding-top:70px}
.brands .wrap{display:flex;align-items:center}
.brands-label{width:200px;font-size:17px;font-weight:600;color:#222}
.brand-name{font-size:24px;font-weight:700;color:#1d3f78;text-align:center;width:240px}
.brand-name.red{color:#b32126}
.brand-name.blue{color:#2b6fb5}

/* footer */
.footer{height:298px;background:radial-gradient(circle at 40% 30%,#262626,#080808 75%);color:#aaa;font-size:12.5px;line-height:1.45}
.footer .wrap{display:flex;padding-top:40px;height:298px}
.fcol{border-right:1px solid var(--line);padding:0 12px}
.fcol:last-child{border-right:none}
.fcol-1{width:300px;padding-left:8px}
.fcol-2{width:320px;padding-left:28px}
.fcol-3{padding-left:28px}
.fbrand{display:flex;align-items:center;gap:8px;color:#ddd;font-weight:700;font-size:17px;line-height:1;text-transform:uppercase;margin-bottom:20px}
.fbrand i{width:36px;height:36px;border-radius:50%;background:var(--orange)}
.fbrand small{display:block;font-size:17px;color:#aaa}
.socials{display:flex;gap:6px;margin-bottom:80px}
.socials i{width:17px;height:17px;border-radius:50%;background:var(--orange)}
</style>
</head>
<body>

<div class="topbar"><div class="wrap">
  <span>Deutsche Markenqualität</span><span>25 Jahre Garantie</span><span>Schnelle Lieferung</span><span class="active">Kostenlose Fachberatung</span><span>Bundesweiter Montageservice</span>
</div></div>

<header class="header"><div class="wrap">
  <div class="brand"><span class="brand-dot"></span><div>Brunnfeld<small>Bauwaren</small></div></div>
  <div class="phone"><strong>08143/618 372 0</strong><span>Mo. – Fr. von 09:00 bis 18:00 Uhr</span></div>
  <div class="seal" role="img" aria-label="Gütesiegel"></div>
  <div class="account"><div><i></i><a>Mein Konto</a></div><div><i></i><a>Warenkorb</a></div></div>
</div></header>

<nav class="nav"><div class="wrap">
  <span class="nav-item">Online-Shop ▾</span><span class="nav-item dark">Service ▾</span>
  <div class="nav-search"><span>Search</span><b></b></div>
</div></nav>

<section class="hero"><div class="wrap">
  <h1>Edelstahlschornstein</h1>
  <div class="hero-frame"><div class="hero-photo" role="img" aria-label="Foto eines Hauses mit rotem Ziegeldach und Edelstahlschornstein"></div></div>
  <div class="hero-copy">
    <h2>Alle Edelstahlschornsteine hergestellt in Deutschland mit 25 Jahren Garantie.</h2>
    <ul>
      <li><svg class="tick" viewBox="0 0 20 20"><circle cx="10" cy="10" r="8.5" fill="none" stroke="#f26b1d" stroke-width="2"/><path d="M6 10.5l3 3 5-6" fill="none" stroke="#f26b1d" stroke-width="2"/></svg>Top Beratung</li>
      <li><svg class="tick" viewBox="0 0 20 20"><circle cx="10" cy="10" r="8.5" fill="none" stroke="#f26b1d" stroke-width="2"/><path d="M6 10.5l3 3 5-6" fill="none" stroke="#f26b1d" stroke-width="2"/></svg>Bestpreisgarantie</li>
      <li><svg class="tick" viewBox="0 0 20 20"><circle cx="10" cy="10" r="8.5" fill="none" stroke="#f26b1d" stroke-width="2"/><path d="M6 10.5l3 3 5-6" fill="none" stroke="#f26b1d" stroke-width="2"/></svg>Schnelle Lieferung</li>
    </ul>
    <div class="cta"><span class="btn">JETZT ENTDECKEN</span><em>&gt;&gt;&gt;</em></div>
  </div>
</div></section>

<section class="intro"><div class="wrap">
  <h3>Edelstahlschornsteine, Schornsteinverlängerungen, Ofenrohre und Schornstein Zubehör – alles bei brunnfeld-bauwaren.de günstig kaufen.</h3>
  <p>Kann ich einen Edelstahlschornstein im Internet kaufen? Diese Frage haben Sie sich bestimmt noch nie gestellt. Bei anderen Waren ist das eine Selbstverständlichkeit, aber bei einem Edelstahlkamin denkt man zunächst nicht ans Onlineshopping. Dabei gibt es schon seit einigen Jahren diverse Plattformen die alles rund um das Thema Edelstahlschornstein anbieten. Allerdings betreiben diese Anbieter ihre Webshops nur nebenher. Dies spiegelt sich in der schlechten Benutzerfreundlichkeit und der teilweise stark veralteten Technik der Seiten wieder. Brunnfeld Bauwaren ist hier einen neuen Weg gegangen. Das Ziel war es, einen Onlineshop für Edelstahlschornsteine und Schornstein Zubehör auf die Beine zu stellen, der nicht nur professionell und nach dem neuesten Stand der Technik aufgebaut ist, sondern Ihnen auch die Sicherheit und Usability bietet, die Sie von großen Onlineplattformen anderer Branchen gewohnt sind. Mit einer effizienten Organisation, modernster Technik und jahrelanger Erfahrung mit dem Produkt Edelstahlschornstein, konnte dieser Anspruch erfüllt werden. Beste Usability, geprüfter Datenschutz, hochwertige Waren und eine kompetente telefonische Beratung runden Ihr Einkaufserlebnis bei Brunnfeld Bauwaren ab.</p>
  <p>Edelstahlschornstein, Schornstein Bausatz und Edelstahlkamin – alles aus einer Hand.</p>
  <p>Ob Sie einen doppelwandigen Edelstahlschornstein, eine Schornsteinsanierung für Ihren alten gemauerten Kamin oder einen Schornstein Bausatz für Ihr Haus suchen: hier werden Sie fündig. Bei Brunnfeld Bauwaren finden Sie eine große Auswahl an in Deutschland hergestellter Edelstahlschornsteine des Herstellers Veltras. Diese Schornsteine werden nach modernsten Produktionsmethoden aus hochwertigem V4A Edelstahl hergestellt und unterliegen strengsten Qualitätsvorschriften. Die Veltras GmbH gewährt Ihnen darüber hinaus auch eine Garantie von 25 Jahren auf jeden in diesem Onlineshop erworbenen Edelstahlschornstein. Ganz einfach: Sicherheit zum besten Preis!</p>
  <a class="readmore">Read more&gt;&gt;&gt;</a>
</div></section>

<section class="features"><div class="wrap">
  <div class="feature">
    <svg class="feature-icon" viewBox="0 0 76 76"><circle cx="38" cy="38" r="36" fill="#111" stroke="#f26b1d" stroke-width="2"/><circle cx="38" cy="38" r="29" fill="#f26b1d"/><circle cx="38" cy="38" r="15" fill="none" stroke="#fff" stroke-width="3"/><path d="M38 30v9h7" fill="none" stroke="#fff" stroke-width="3"/></svg>
    <h4>Beratung</h4><p>Lassen Sie sich jetzt von unseren<br>Profis beraten - kostenlos -</p><a>Jetzt Entdecken&gt;&gt;&gt;</a>
  </div>
  <div class="feature">
    <svg class="feature-icon" viewBox="0 0 76 76"><circle cx="38" cy="38" r="36" fill="#111" stroke="#f26b1d" stroke-width="2"/><circle cx="38" cy="38" r="29" fill="#f26b1d"/><path d="M24 38l14-12 14 12M28 35v14h20V35" fill="none" stroke="#fff" stroke-width="3" stroke-linejoin="round"/><rect x="35" y="41" width="6" height="8" fill="#fff"/></svg>
    <h4>Montageservice</h4><p>Bundesweite Edelstahlschornsteinmontage<br>vom Profi zum unschlagbaren Festpreis</p><a>Vorteilspreis sichern&gt;&gt;&gt;</a>
  </div>
  <div class="feature">
    <svg class="feature-icon" viewBox="0 0 76 76"><circle cx="38" cy="38" r="36" fill="#111" stroke="#f26b1d" stroke-width="2"/><circle cx="38" cy="38" r="29" fill="#f26b1d"/><rect x="28" y="26" width="20" height="25" rx="2" fill="none" stroke="#fff" stroke-width="3"/><rect x="33" y="23" width="10" height="5" fill="#fff"/><path d="M32 39l4 4 7-8" fill="none" stroke="#fff" stroke-width="3"/></svg>
    <h4>Marketing</h4><p>Brunnfeld Bauwaren Produkt<br>- berater</p><a>Beratung gewinnbaren&gt;&gt;&gt;</a>
  </div>
</div></section>

<section class="products"><div class="wrap">
  <div class="grid">
    <div class="card-featured">
      <div class="shot" role="img" aria-label="Foto eines Kaminofens mit Holzstapel vor heller Wand" style="background:linear-gradient(90deg,#d8cdbf 0%,#8a6a47 30%,#efe9e1 50%,#2a2a2a 70%,#e0d7cc 100%)"></div>
      <div class="caption cap-big"><h5>Kaminofen</h5><span class="stars">★★★★</span><p>Kaminofen mit hervorragendem Preis- / Leistungsverhältnis versandkostenfrei online bestellen. Langlebige Qualität und Sicherheit für Ihr Haus.</p></div>
      <span class="feat-price">$1599,00</span>
      <span class="feat-title">Kaminofen Nordhaven 5kW</span>
      <span class="feat-buy">JETZT ANSEHEN</span>
      <p class="feat-text">Kaminofen Nordhaven mit einer Nennwärmeleistung von 5kW. Für ein qualitatives und erholsames Wohlbefinden. Erhältlich mit stilvollen, naturgetreuen Seitenverkleidungen. Abdeckung und Wärmefach in hochwertiger Sandsteinverkleidung. Einfache Luftregelung. Mit einem optimalen Raumheizvermögen bis zu 170 Kubikmeter.</p>
      <a class="feat-more">Read more&gt;&gt;&gt;</a>
    </div>
    <div class="card"><div class="shot" role="img" aria-label="Foto eines Kaminofens vor Fliesenwand" style="background:linear-gradient(160deg,#efe8dc,#c9bba6 60%,#3b3b3b)"></div><div class="card-bar"><span class="see">JETZT ANSEHEN</span><span class="price">$1779,00</span></div></div>
    <div class="card"><div class="shot" role="img" aria-label="Foto eines grauen Kaminofens im Wohnraum" style="background:linear-gradient(160deg,#6f6a3a,#b9b6aa 55%,#e2ded4)"></div><div class="card-bar"><span class="see">JETZT ANSEHEN</span><span class="price">$1123,00</span></div></div>
    <div class="card"><div class="shot" role="img" aria-label="Foto eines Kaminofens mit Holzverkleidung" style="background:linear-gradient(160deg,#e9e2d6,#c28b4b 50%,#3a3a3a)"></div><div class="card-bar"><span class="see">JETZT ANSEHEN</span><span class="price">$1588,00</span></div></div>
    <div class="card"><div class="shot" role="img" aria-label="Foto eines Kaminofens vor Steinwand" style="background:linear-gradient(160deg,#a9927a,#5e5147 50%,#2a2a2a)"></div><div class="card-bar"><span class="see">JETZT ANSEHEN</span><span class="price">$188,00</span></div></div>
  </div>
  <div class="divider"></div>
  <div class="row4">
    <div class="card"><div class="shot" role="img" aria-label="Foto eines Kaminofens mit Holzfach" style="background:linear-gradient(160deg,#e7e4dc,#a8a59a 50%,#c28b4b)"></div><div class="card-bar"><span class="see">JETZT ANSEHEN</span><span class="price">$1697,00</span></div></div>
    <div class="card"><div class="shot" role="img" aria-label="Foto eines schwarzen Kaminofens vor Steinwand" style="background:linear-gradient(160deg,#c2b3a0,#4a4440 50%,#1e1e1e)"></div><div class="card-bar"><span class="see">JETZT ANSEHEN</span><span class="price">$1009,00</span></div></div>
    <div class="card"><div class="shot" role="img" aria-label="Foto eines Kaminofens im grünen Wohnraum" style="background:linear-gradient(160deg,#7c7a40,#b8b5a7 60%,#ddd8cc)"></div>
      <div class="caption cap-small"><h5>Kaminofen</h5><span class="stars">★★★★★</span><p>Kaminofen mit hervorragendem Preis- / Leistungsverhältnis versandkostenfrei online bestellen. Langlebige Qualität und Sicherheit für Ihr Haus.</p></div>
      <div class="card-bar"><span class="see hot">JETZT ANSEHEN</span><span class="price">$1999,00</span></div></div>
    <div class="card"><div class="shot" role="img" aria-label="Foto eines Kaminofens mit Holzstapel" style="background:linear-gradient(160deg,#efe9e0,#b39b7c 50%,#3a3a3a)"></div><div class="card-bar"><span class="see">JETZT ANSEHEN</span><span class="price">$1697,00</span></div></div>
  </div>
</div></section>

<section class="secure"><div class="wrap">
  <div class="secure-row">
    <div class="secure-label">Sicher Einkaufen</div>
    <div class="flag-badge" role="img" aria-label="Herkunftssiegel"></div>
    <p class="secure-text">Wir bieten ausschließlich Waren von deutschen Markenherstellern an. Unser gesamtes Sortiment wird von Branchenführern hergestellt und unterliegt ständigen Qualitätskontrollen. Für Ihre Sicherheit nur das Beste zum fairen Preis.</p>
    <div class="round-badge" role="img" aria-label="Garantiesiegel"></div>
    <p class="secure-text">Um unserem Premiumanspruch und unserem Leistungsversprechen gerecht zu werden, erhalten Sie bei uns selbstverständlich 25 Jahre Garantie auf alle Edelstahlschornsteine und Edelstahlschornstein Bauteile.</p>
  </div>
  <div class="pay-row">
    <div class="secure-label">Zahlungsarten</div>
    <div class="pays"><span class="pay">Kartenpay</span><span class="pay">Vireo</span><span class="pay">Paywell</span><span class="pay">Sofortly</span><span class="pay">Vorkasse</span><span class="pay">Amerion</span><span class="pay">Lastschrift</span></div>
  </div>
</div></section>

<section class="brands"><div class="wrap">
  <div class="brands-label">Unsere Marken</div>
  <span class="brand-name">veltras</span><span class="brand-name blue">Rondel</span><span class="brand-name red">Hallert + Moos</span>
</div></section>

<footer class="footer"><div class="wrap">
  <div class="fcol fcol-1">
    <div class="fbrand"><i></i><div>Brunnfeld<small>Bauwaren</small></div></div>
    <p>Kontorwerk GmbH<br>Lindenweg 27<br>80331 München<br>Deutschland</p><br>
    <p>Brunnfeld Bauwaren<br>Durchschnittliche Bewertung: 4.71 (von 5).<br>Ermittelt aus 265 Bewertungen.</p>
  </div>
  <div class="fcol fcol-2">
    <p>Häufige Fragen<br>AGB<br>Lieferung &amp; Zahlung<br>Impressum<br>Blog</p><br>
    <p>Über uns<br>Widerruf<br>Datenschutz<br>Kontaktieren Sie uns<br>Glossar</p>
  </div>
  <div class="fcol fcol-3">
    <div class="socials"><i></i><i></i><i></i><i></i></div>
    <p>Kostenlose Beratung</p><br>
    <p>08143 / 618 372 0<br>Mo. – Fr. von 09:00 bis 18:00 Uhr<br>info@brunnfeld-bauwaren.de</p>
  </div>
</div></footer>

</body>
</html>
```